Letterhead for a German Distribution/Manufacturing Company

We need a professional Letterhead in a unique Design.
not to playful.
The Letterhead has to show show that we are a international company with headquater in Germany.
all details like adress, Vat Tax Number, Bank Accout, Eori, email, Company number has to be on the Letterhead.
for example use: VAT TAX DE5704168 Bank Account: Norrfeld Bank IBAN DE421705238ß310482 Swift: KOLV3154802 EORI 3041296587 Company Number: HRB 61508 Adress: VOLTRINA UG Amsel Strasse 7 Postal Code 04683 City Lindenhain Country: Germany Email: info@voltrina-example.com
the design can be colored but doesnt have to be
Industry/Entity Type
Manufacturing and international distribution
Requirements
Must have
- show that we are a international company with headquater in Germany. our company infos and logo

```html
<!DOCTYPE html>
<html lang="en">
<head>
<meta charset="utf-8">
<title>VOLTRINA Letterhead</title>
<link href="https://fonts.googleapis.com/css2?family=Lato:wght@400;700&family=Great+Vibes&display=swap" rel="stylesheet">
<style>
  :root {
    --backdrop: #56667d;
    --paper: #ffffff;
    --ink: #3a3a3a;
    --ink-dark: #2b2b2b;
    --mark: #4a4a4a;
  }
  * { margin: 0; padding: 0; box-sizing: border-box; }
  html, body {
    width: 1200px; height: 725px; overflow: hidden;
    background: var(--backdrop);
  }
  .sheet {
    position: absolute; left: 350px; top: 21px;
    width: 500px; height: 682px;
    background: var(--paper);
    box-shadow: 0 4px 14px rgba(0,0,0,0.35);
    font-family: "Lato", sans-serif;
    color: var(--ink);
  }
  .brand {
    position: absolute; left: 28px; top: 45px;
    display: flex; align-items: center; gap: 10px;
  }
  .brand-dot {
    width: 40px; height: 40px; border-radius: 50%;
    background: var(--mark);
  }
  .brand-name {
    font-size: 30px; font-weight: 400; letter-spacing: 0.5px;
    color: var(--mark);
  }
  .block {
    position: absolute; left: 28px; width: 445px;
    font-size: 9.4px; line-height: 10.8px;
  }
  .date { top: 173px; }
  .recipient { top: 197px; }
  .company { top: 231px; }
  .salutation { top: 279px; font-size: 11.5px; font-weight: 700; color: var(--ink-dark); line-height: 14px; }
  .body p {
    position: absolute; left: 0; width: 445px;
    text-align: justify; text-align-last: left;
  }
  .body { top: 0; }
  .p1 { top: 307px; }
  .p2 { top: 360px; }
  .p3 { top: 414px; }
  .p4 { top: 457px; }
  .closing { top: 500px; }
  .signature {
    position: absolute; left: 30px; top: 522px;
    font-family: "Great Vibes", cursive;
    font-size: 24px; color: var(--ink-dark);
  }
  .legal {
    position: absolute; left: 25px; top: 594px;
    font-size: 7.4px; line-height: 11.3px; color: var(--ink-dark);
  }
</style>
</head>
<body>
  <main class="sheet">
    <header class="brand">
      <span class="brand-dot"></span>
      <span class="brand-name">VOLTRINA</span>
    </header>

    <div class="block date">January-03-2020</div>
    <div class="block recipient">Mr, Paul Brenner<br>President</div>
    <div class="block company">Arden Corporation<br>123 Street Name, Suite# 10<br>City, State, 120023</div>
    <div class="block salutation">Dear Mr, Paul</div>

    <div class="block body">
      <p class="p1">Lorem ipsum dolor sit amet, consectetur adipisicing elit, sed do eiusmod tempor incididunt ut labore et dolore magna aliqua. Ut enim ad minim veniam, quis nostrud exercitation ullamco laboris nisi ut aliquip ex ea commodo consequat. Duis aute irure dolor in reprehenderit in voluptate velit esse cillum dolore eu fugiat nulla pariatur.</p>
      <p class="p2">Lorem ipsum dolor sit amet, consectetur adipisicing elit, sed do eiusmod tempor incididunt ut labore et dolore magna aliqua. Ut enim ad minim veniam, quis nostrud exercitation ullamco laboris nisi ut aliquip ex ea commodo consequat. Duis aute irure dolor in reprehenderit in voluptate velit esse cillum dolore eu fugiat nulla pariatur.</p>
      <p class="p3">Lorem ipsum dolor sit amet, consectetur adipisicing elit, sed do eiusmod tempor incididunt ut labore et dolore magna aliqua. Ut enim ad minim veniam, quis nostrud exercitation ullamco laboris nisi ut aliquip ex ea commodo consequat.</p>
      <p class="p4">Excepteur sint occaecat cupidatat non proident, sunt in culpa qui officia deserunt mollit anim id est laborum. re et dolore magnam aliquam quaerat voluptatem.</p>
    </div>

    <div class="block closing">Regards</div>
    <div class="signature">Daniel Hartley</div>

    <footer class="legal">
      VAT TAX DE5704168<br>
      Bank Account: Norrfeld Bank IBAN DE421705238ß310482 Swift: KOLV3154802<br>
      EORI 3041296587<br>
      Company Number: HRB 61508<br>
      Adress: VOLTRINA UG Amsel Strasse 7 Postal Code 04683 City Lindenhain Country<br>
      Germany Email: info@voltrina-example.com
    </footer>
  </main>
</body>
</html>
```